Tide Harbor Finance Business Cards

Looking for a business card for a new mortgage broking business. Name of the business is Tide Harbor Finance. Purpose of the business is to build trust and strong relationships with clients to then assist them with your mortgage lending needs. Most relationships within the business start off as an enquiry, and then can evolve into a 10+ year relationship, servicing clients from purchasing a new home to then upgrading for their family and even then assisting their children with their first home purchase. Business card should communicate financial security and trust.

Target Market(s)

Targeting professional clients who are looking to build a relationship with a knowledgeable mortgage professional

Industry/Entity Type

Finance - Home Loans

Contact Information for Business Card

Peter Colburn, Director, mobile: 0427 903186, email:peter@tideharborfinance.com.au, website: www.tideharborfinance.com.au

Font styles to use
Sans Serif

Requirements
Must have
• On the front: Must have company logo, contact details as above. On the back: slogan, 'Smart options, peace of mind', plus listing services offered: home loans, investment loans, first home buyers, refinancing, car finance

```html
<!DOCTYPE html>
<html lang="en">
<head>
<meta charset="utf-8">
<title>Tide Harbor Finance – Business Cards</title>
<link rel="stylesheet" href="https://fonts.googleapis.com/css2?family=Arimo:wght@400;500;700&family=Roboto+Condensed:wght@400&display=swap">
<style>
  :root {
    --backdrop: #adadad;
    --brand-blue: #00527a;
    --brand-orange: #f0a00f;
    --paper: #ffffff;
    --ink: #1f1f1f;
    --rule: #c9c9c9;
  }
  * { box-sizing: border-box; margin: 0; padding: 0; }
  html, body { width: 1093px; height: 1200px; overflow: hidden; }
  body {
    position: relative;
    background: var(--backdrop);
    font-family: "Arimo", Arial, sans-serif;
  }
  .card {
    position: absolute;
    left: 265px;
    width: 580px;
    height: 357px;
    border-radius: 26px;
    overflow: hidden;
  }
  /* ---------- front ---------- */
  .card-front {
    top: 226px;
    background: var(--paper);
  }
  .card-front .edge-band {
    position: absolute;
    left: 0; right: 0; bottom: 0;
    height: 7px;
    background: var(--brand-blue);
  }
  .brand {
    position: absolute;
    display: flex;
    align-items: center;
  }
  .brand-mark { flex: none; }
  .brand-name {
    font-weight: 500;
    text-transform: uppercase;
    line-height: 1.02;
  }
  .card-front .brand { left: 52px; top: 131px; gap: 12px; }
  .card-front .brand-mark { width: 72px; height: 72px; background: var(--brand-blue); border-radius: 7px; }
  .card-front .brand-name { color: var(--brand-blue); font-size: 27px; }

  .divider {
    position: absolute;
    left: 270px; top: 74px;
    width: 1px; height: 209px;
    background: var(--rule);
  }
  .person { position: absolute; left: 288px; top: 116px; }
  .person-name {
    color: var(--brand-blue);
    font-size: 24px;
    font-weight: 400;
    letter-spacing: 0.2px;
  }
  .person-name strong { font-weight: 700; }
  .person-role {
    color: var(--brand-orange);
    font-size: 17px;
    margin-top: 1px;
  }
  .contacts {
    position: absolute;
    left: 288px; top: 174px;
    list-style: none;
  }
  .contacts li {
    display: flex;
    align-items: center;
    gap: 9px;
    height: 21px;
    font-size: 16.5px;
    color: var(--ink);
  }
  .contacts svg { width: 15px; height: 15px; flex: none; }
  .contacts .domain { color: var(--brand-blue); }

  /* ---------- back ---------- */
  .card-back {
    top: 621px;
    background: var(--brand-blue);
    color: var(--paper);
    text-align: center;
  }
  .card-back .brand { left: 150px; top: 62px; gap: 22px; }
  .card-back .brand-mark { width: 105px; height: 105px; background: var(--paper); border-radius: 12px; }
  .card-back .brand-name { color: var(--paper); font-size: 40px; text-align: left; }
  .tagline {
    position: absolute;
    left: 0; right: 0; top: 228px;
    color: var(--brand-orange);
    font-size: 18px;
    font-weight: 700;
    letter-spacing: 0.3px;
  }
  .services-heading {
    position: absolute;
    left: 42px; right: 42px; top: 283px;
    display: flex;
    align-items: center;
    gap: 8px;
    font-size: 17px;
    font-weight: 700;
    letter-spacing: 0.3px;
    white-space: nowrap;
  }
  .services-heading::before,
  .services-heading::after {
    content: "";
    flex: 1;
    height: 1.5px;
  }
  .services-heading::before { background: linear-gradient(to right, transparent, var(--brand-orange) 35%); }
  .services-heading::after { background: linear-gradient(to left, transparent, var(--brand-orange) 35%); }
  .services-list {
    position: absolute;
    left: 0; right: 0; top: 305px;
    list-style: none;
    display: flex;
    justify-content: center;
    align-items: center;
    font-family: "Roboto Condensed", "Arial Narrow", sans-serif;
    font-size: 17px;
    white-space: nowrap;
  }
  .services-list li + li::before {
    content: "";
    display: inline-block;
    width: 5px; height: 5px;
    margin: 0 4px 2px;
    border-radius: 50%;
    background: var(--brand-orange);
    vertical-align: middle;
  }
</style>
</head>
<body>

  <section class="card card-front" aria-label="Business card front">
    <div class="brand">
      <span class="brand-mark" aria-hidden="true"></span>
      <span class="brand-name">Tide<br>Harbor<br>Finance</span>
    </div>

    <div class="divider"></div>

    <div class="person">
      <p class="person-name"><strong>PETER</strong> COLBURN</p>
      <p class="person-role">Director</p>
    </div>

    <ul class="contacts">
      <li>
        <svg viewBox="0 0 16 16" aria-hidden="true"><path d="M4 1.5l2.2 2.6-1.3 1.6c.8 2 2.4 3.6 4.4 4.4l1.6-1.3 2.6 2.2-1.3 2.3C7 13.4 2.6 9 2.2 3L4 1.5z" fill="var(--brand-blue)"/><path d="M9.5 2.5a4 4 0 014 4M9.5 0.6a6 6 0 016 6" fill="none" stroke="var(--brand-blue)" stroke-width="1.2"/></svg>
        <span>0427 903186</span>
      </li>
      <li>
        <svg viewBox="0 0 16 16" aria-hidden="true"><rect x="0.5" y="3" width="15" height="10" fill="var(--brand-blue)"/><path d="M0.5 3.5L8 9l7.5-5.5M0.5 12.5l5.5-5M15.5 12.5l-5.5-5" fill="none" stroke="#fff" stroke-width="1.1"/></svg>
        <span>peter@tideharborfinance.com.au</span>
      </li>
      <li>
        <svg viewBox="0 0 16 16" aria-hidden="true"><g fill="none" stroke="var(--brand-blue)" stroke-width="1.2"><circle cx="8" cy="8" r="6.8"/><ellipse cx="8" cy="8" rx="3" ry="6.8"/><path d="M1.2 8h13.6M2.5 4.5h11M2.5 11.5h11"/></g></svg>
        <span>www.<span class="domain">tideharborfinance</span>.com.au</span>
      </li>
    </ul>

    <div class="edge-band"></div>
  </section>

  <section class="card card-back" aria-label="Business card back">
    <div class="brand">
      <span class="brand-mark" aria-hidden="true"></span>
      <span class="brand-name">Tide<br>Harbor<br>Finance</span>
    </div>

    <p class="tagline">SMART OPTIONS, PEACE OF MIND</p>

    <h2 class="services-heading">SERVICES OFFERED</h2>
    <ul class="services-list">
      <li>Home Loans</li>
      <li>Investment Loans</li>
      <li>First Home Buyers</li>
      <li>Refinancing</li>
      <li>Car Finance</li>
    </ul>
  </section>

</body>
</html>
```